Cognitive therapist.

I am a therapist and my main work is with clients who have depression and anxiety disorders.

I need something reasonably plain. Cognitive therapy is a very pragmatic approach to dealing with problems, so it isn't new agey (no offence to new age therapies at all)

Hi everyone, I am currently looking at a particular design that I will most likely go with. Cheers, Mel

Mel Tarrow
Cognitive Therapist
BA, PG Dip Mental Health,
PG Dip Cog Beh Therapy
MKLPT

The Larchmont Rooms,
Level One
57 Quillon Parade
Cnr Fenwick St & Quillon Parade
P O Box 38 215
WELLINGTON 6281

Phone: 027 534 2870 Email: mtarrow@vexmail.co.nz

www.meltarrow.co.nz

• No illustration, or colour. not old style fonts.

```html
<!DOCTYPE html>
<html lang="en">
<head>
<meta charset="utf-8">
<title>Mel Tarrow – Business Card</title>
<link rel="stylesheet" href="https://fonts.googleapis.com/css2?family=Questrial&display=swap">
<style>
  :root {
    --teal: #6ec8cd;
    --ink: #555555;
    --card: #ffffff;
    --backdrop: #ebebeb;
  }
  * { margin: 0; padding: 0; box-sizing: border-box; }
  html, body {
    width: 1200px;
    height: 1200px;
    overflow: hidden;
    background: var(--backdrop);
  }
  .card {
    position: absolute;
    left: 25px;
    top: 268px;
    width: 1150px;
    height: 663px;
    background: var(--card);
    border-radius: 46px;
    overflow: hidden;
    font-family: "Questrial", "Century Gothic", sans-serif;
    color: var(--ink);
    box-shadow: 0 6px 24px rgba(0,0,0,0.12);
  }
  .identity {
    position: absolute;
    right: 602px;
    top: 226px;
    text-align: right;
  }
  .identity__name {
    font-size: 74px;
    line-height: 74px;
    font-weight: 400;
    color: var(--teal);
    letter-spacing: 1px;
    white-space: nowrap;
  }
  .identity__credentials {
    margin-top: 6px;
    font-size: 25px;
    line-height: 35px;
    white-space: nowrap;
  }
  .divider {
    position: absolute;
    left: 576px;
    top: 218px;
    width: 2px;
    height: 217px;
    background: var(--ink);
  }
  .contact {
    position: absolute;
    left: 619px;
    top: 207px;
    font-size: 25px;
    line-height: 35.5px;
    white-space: nowrap;
  }
  .contact__po {
    margin-top: 7px;
  }
  .contact__po b {
    font-weight: 700;
    font-family: Arial, sans-serif;
    font-size: 24px;
  }
  .contact__row {
    display: flex;
    align-items: center;
    gap: 5px;
    height: 36px;
  }
  .contact__row--phone { margin-top: 9px; }
  .contact__icon { width: 28px; height: 28px; flex: none; }
  .footer-band {
    position: absolute;
    top: 603px;
    height: 15px;
    background: var(--teal);
  }
  .footer-band--left { left: 0; width: 390px; }
  .footer-band--right { left: 783px; width: 367px; }
  .website {
    position: absolute;
    left: 390px;
    width: 393px;
    top: 591px;
    text-align: center;
    font-size: 30px;
    line-height: 36px;
  }
</style>
</head>
<body>
  <div class="card">
    <div class="identity">
      <h1 class="identity__name">MEL TARROW</h1>
      <p class="identity__credentials">
        Cognitive Therapist BA,<br>
        PG Dip Mental Health,<br>
        PG Dip Cog Beh Therapy MKLPT
      </p>
    </div>

    <div class="divider"></div>

    <div class="contact">
      <p class="contact__address">
        The Larchmont Rooms, Level One<br>
        57 Quillon Parade Cnr Fenwick St<br>
        &amp; Quillon Parade
      </p>
      <p class="contact__po"><b>P O</b> Box 38 215 WELLINGTON 6281</p>
      <div class="contact__row contact__row--phone">
        <svg class="contact__icon" viewBox="0 0 28 28" aria-label="Phone">
          <circle cx="14" cy="14" r="13" fill="var(--teal)"/>
          <rect x="9.5" y="6" width="9" height="16" rx="1.8" fill="none" stroke="#fff" stroke-width="1.6"/>
          <rect x="11.3" y="8.2" width="5.4" height="8" fill="#fff"/>
          <circle cx="14" cy="19.2" r="1" fill="#fff"/>
        </svg>
        <span>027 534 2870</span>
      </div>
      <div class="contact__row">
        <svg class="contact__icon" viewBox="0 0 28 28" aria-label="Email">
          <circle cx="14" cy="14" r="13" fill="var(--teal)"/>
          <rect x="7" y="9" width="14" height="10" rx="1" fill="#fff"/>
          <path d="M7.5 9.6 L14 15 L20.5 9.6" fill="none" stroke="var(--teal)" stroke-width="1.4"/>
        </svg>
        <span>mtarrow@vexmail.co.nz</span>
      </div>
    </div>

    <div class="footer-band footer-band--left"></div>
    <p class="website">www.meltarrow.co.nz</p>
    <div class="footer-band footer-band--right"></div>
  </div>
</body>
</html>
```